Guaranteed Job - Sleek Sexy Business Card UV Spot

Im looking for a sleek and sexy business card, that resembles elite or VIP status status.
our business is corinvale.example
you can view our products on there, but our main audience for handing out our cards will be for people in the hospitality industry, so it will need to impress high management and CEO of hotels and restaurants, bars, clubs etc...
the card features will have UV spot on both sides, 400gsm stock. standard size.
Artwork should be 86 x 54mm + 2mm bleed = 90 x 58mm
it should have a nice "unique" uv spot pattern that highlights the card, not a repeated pattern, theres no originality there, and it will be disregarded.
The written material will be:
Corin Vale Hospitality College (logo)
Tobin Marsh
Director
Phone: 1300 615 737
Mobile: 0455 817 296
Email: info@corinvale.example
website: www.corinvale.example
I'm looking for originality here, i don't want just a simple stock card, want something that has a wow factor for people.
You will find the logo attached. you may invert the white to black words to suit the background as you please.
thank you and good luck
As a side note, ive received a lot of proposals, im too busy to give feedback to each and every one, so if i havent provided feedback for your design within 24 hours, then consider it not acceptable, and you could resubmit another design.
So far i have not seen any design that stood out for me, they all seem pretty generic. there nothing thats unique, i would figure for the amount that im offering, that people would put some more effort and creativity into the design.
so far over 200 designs submitted, and nothing i have seen looks very original, everything looks like a different variation of the same stuff, i said it very clearly i wanted something unique, the only thing that has come close to it so far is this one
Reason: Ive received alot of design concepts and i have reviewed everyone, but i havent had time to give feedback to every single one, only the ones that have interested me, if i havent responded, its because i havent found it good enough.
so far only a few design have been on par with what ive been looking for, an attractive eye popping design.
heres a few of them,
http://files.pixelbazaar.example/design_img/51736/62418/62418_2840915_51736_image.jpg
http://files.pixelbazaar.example/design_img/51736/68254/68254_2841377_51736_image.jpg
theyre, both unique and original, and eye catching, the only thing theyre missing is the sexyness.
if you still think you have some creativity left in your minds, then throw it on here.
Reason: Sorry guys for the delay, I was in a serious accident and out of commission for the past few months, I'm just slowly recovering now, please bare with me as i try to attend to this project, it may take me awhile as I have other projects that are on standby, I'm not 100% at the moment, so im extending the deadline for 2 weeks right now. Thanks for your patience.
Hospitality

```html
<!DOCTYPE html>
<html lang="en">
<head>
<meta charset="utf-8">
<title>Tobin Marsh — Corin Vale Hospitality College</title>
<link rel="stylesheet" href="https://fonts.googleapis.com/css2?family=Fredoka:wght@600;700&family=Share+Tech+Mono&display=swap">
<style>
  :root {
    --deep-blue: #0a3fb8;
    --mid-blue: #1f74d8;
    --sky-cyan: #5ae6f0;
    --ice-blue: #6fd0ff;
    --label-blue: #8fd6ff;
    --white: #ffffff;
    --divider: rgba(170, 225, 255, 0.75);
  }
  html, body {
    margin: 0;
    padding: 0;
    width: 1200px;
    height: 686px;
    overflow: hidden;
    background: #ffffff;
  }
  .card {
    position: relative;
    width: 1200px;
    height: 686px;
    overflow: hidden;
    background:
      radial-gradient(circle at 1000px 115px, rgba(255,255,255,0.55) 0, rgba(255,255,255,0) 14px),
      radial-gradient(circle at 1068px 550px, rgba(255,255,255,0.7) 0, rgba(255,255,255,0) 22px),
      radial-gradient(circle at 940px 390px, rgba(255,255,255,0.45) 0, rgba(255,255,255,0) 18px),
      radial-gradient(circle at 120px 110px, rgba(255,255,255,0.35) 0, rgba(255,255,255,0) 16px),
      radial-gradient(circle at 860px 600px, rgba(255,255,255,0.35) 0, rgba(255,255,255,0) 18px),
      radial-gradient(circle at 612px 590px, rgba(120,255,255,0.6) 0, rgba(120,255,255,0) 10px),
      radial-gradient(circle at 18px 568px, rgba(120,255,255,0.6) 0, rgba(120,255,255,0) 10px),
      radial-gradient(ellipse 520px 380px at 1180px 40px, rgba(90,230,240,0.95), rgba(90,230,240,0) 100%),
      radial-gradient(ellipse 600px 420px at 180px 360px, rgba(5,40,140,0.55), rgba(5,40,140,0) 100%),
      linear-gradient(120deg, var(--deep-blue) 0%, var(--mid-blue) 45%, #3aa8ec 75%, var(--sky-cyan) 100%);
    font-family: "Share Tech Mono", monospace;
  }
  .divider {
    position: absolute;
    left: 571px;
    top: 150px;
    width: 2px;
    height: 400px;
    background: linear-gradient(to bottom, rgba(170,225,255,0), var(--divider) 15%, var(--divider) 85%, rgba(170,225,255,0));
  }
  .brand {
    position: absolute;
    left: 600px;
    top: 112px;
    display: flex;
    align-items: center;
    gap: 28px;
  }
  .brand-dot {
    width: 150px;
    height: 150px;
    border-radius: 50%;
    background: var(--ice-blue);
    opacity: 0.85;
  }
  .brand-name {
    margin: 0;
    font-family: "Fredoka", sans-serif;
    font-weight: 600;
    color: var(--white);
    line-height: 1.02;
    text-transform: uppercase;
  }
  .brand-name .line-main { display: block; font-size: 66px; letter-spacing: 1px; }
  .brand-name .line-sub { display: block; font-size: 27px; letter-spacing: 1px; }
  .person {
    position: absolute;
    right: 640px;
    top: 272px;
    text-align: right;
    font-family: "Fredoka", sans-serif;
  }
  .person-name {
    margin: 0;
    font-size: 58px;
    font-weight: 700;
    line-height: 1;
    color: var(--white);
    letter-spacing: 1px;
  }
  .person-name .surname { color: var(--ice-blue); }
  .person-role {
    margin: 8px 0 0;
    font-size: 30px;
    font-weight: 600;
    color: var(--white);
  }
  .contacts {
    position: absolute;
    right: 640px;
    top: 418px;
    margin: 0;
    text-align: right;
  }
  .contact-row {
    margin: 0;
    font-size: 25px;
    line-height: 37px;
    color: var(--white);
    letter-spacing: 3px;
    white-space: nowrap;
  }
  .contact-row.gap { margin-top: 20px; }
  .contact-label {
    color: var(--label-blue);
    font-variant: small-caps;
    letter-spacing: 3px;
  }
  .contact-row.web { font-size: 20px; letter-spacing: 3px; }
  .contact-row.web .contact-label { font-size: 25px; }
</style>
</head>
<body>
  <div class="card">
    <div class="divider"></div>

    <div class="brand">
      <div class="brand-dot"></div>
      <p class="brand-name">
        <span class="line-main">Corin Vale</span>
        <span class="line-sub">Hospitality College</span>
      </p>
    </div>

    <div class="person">
      <h1 class="person-name">Tobin <span class="surname">Marsh</span></h1>
      <p class="person-role">Director</p>
    </div>

    <div class="contacts">
      <p class="contact-row"><span class="contact-label">Phone:</span> 1300 615 737</p>
      <p class="contact-row"><span class="contact-label">Mobile:</span> 0455 817 296</p>
      <p class="contact-row web gap"><span class="contact-label">Email:</span> info@corinvale.example</p>
      <p class="contact-row web"><span class="contact-label">Website:</span> www.corinvale.example</p>
    </div>
  </div>
</body>
</html>
```